Investment website design - investing in mutual funds

I need a design of a website (only homepage for now) dedicated to investment in mutual funds. Attached is a mock up with all the elements the homepage design should contain. The homepage should contain a logo in the upper left corner, the domain the website will run on is www.perovalstrinka.cz , in the upper right corner there should be 2 buttons or links SIGN UP / SIGN IN. The bottom of the homepage should contain links to ABOUT US, FAQ, PRIVACY POLICY, CONTACT US.
Now the main elements on the homepage
1) Video that will explain how the investment works exactly, under this video we will have 3 illustrated icons like the ones attached (see 2nd attachement) that will show the potential investor what exactly they could get when investing with us (education for kids, happy life after they retire, regular monthly payment for the rest of their life).
2) On the right side next to the video we will have a calculator where a potential investor can play with the numbers, the investor can fill in the MONTHLY PAYMENT that he wants to invest regularly every month, the time frame of the investment - for how long he wants to invest. Once the potential investor selects those 2 variables we will calculate for him 2 options - either he can get a ONE TIME PAYOUT once he reaches his investment horizon or he can get a regular monthly payment for the rest of his life. Under the laculator there will be a button 'I want to invest ->'. The functionality of the calculator should be similar to the calculator that can be found here http://www.brodavbank.cz/brodav-podilove-fondy/ and https://felbo.cz/.
The design should look similar to https://felbo.cz/ (font, colors, logo). We prefer white background in the area where we have the video and calculator. We also like the design of www.tarvupo.com. Let me know if you have any questions.

```html
<!DOCTYPE html>
<html lang="en">
<head>
<meta charset="utf-8">
<title>perovalstrinka – Investing in mutual funds</title>
<link href="https://fonts.googleapis.com/css2?family=Roboto+Slab:wght@400;500;700&display=swap" rel="stylesheet">
<style>
  :root {
    --teal: #42b1bf;
    --teal-dark: #2e8f9c;
    --field: #bde2e4;
    --field-text: #2a8c99;
    --accent: #e9553a;
    --accent-shadow: #2f8e9a;
    --white: #ffffff;
    --ink: #4a4a4a;
    --footer-bar: #4f4d50;
    --screen-dark: #0f0f10;
  }
  * { box-sizing: border-box; margin: 0; padding: 0; }
  html, body { width: 1200px; height: 635px; overflow: hidden; background: var(--white); }
  body { font-family: "Roboto Slab", Georgia, serif; position: relative; }

  .hero { position: absolute; left: 0; top: 0; width: 1200px; height: 488px; background: var(--teal); }

  .brand { position: absolute; left: 58px; top: 12px; color: var(--white); font-weight: 700; font-size: 18px; letter-spacing: 0.2px; }

  .account-nav { position: absolute; top: 15px; left: 1002px; display: flex; gap: 9px; }
  .btn-small {
    display: block; width: 60px; height: 23px; line-height: 23px; text-align: center;
    background: var(--accent); color: var(--white); font-size: 9px; font-weight: 700;
    text-decoration: none; box-shadow: 4px 4px 0 var(--accent-shadow);
  }

  .video-monitor { position: absolute; left: 51px; top: 102px; width: 560px; height: 426px; }
  .monitor-visual {
    position: absolute; left: 0; top: 0; width: 560px; height: 340px; border-radius: 10px;
    background: var(--screen-dark); padding: 22px 22px 27px;
  }
  .monitor-visual .screen {
    width: 100%; height: 100%;
    background: linear-gradient(160deg, #a7a39f 0%, #6d6a6b 45%, #2a2c35 100%);
    position: relative;
  }
  .monitor-stand {
    position: absolute; left: 195px; top: 340px; width: 171px; height: 86px;
    background: linear-gradient(90deg, #9b9b9d, #e6e6e7 50%, #9b9b9d);
    clip-path: polygon(18% 0, 82% 0, 86% 90%, 100% 96%, 100% 100%, 0 100%, 0 96%, 14% 90%);
  }
  .play-icon { position: absolute; left: 50%; top: 50%; transform: translate(-50%, -50%); }

  .calculator { position: absolute; left: 683px; top: 96px; width: 452px; color: var(--white); }
  .calculator h1 { font-size: 29px; font-weight: 700; line-height: 1; letter-spacing: 0.2px; }
  .field {
    display: block; width: 448px; height: 31px; margin-left: 2px; background: var(--field);
    color: var(--field-text); font-size: 11px; line-height: 31px; padding-left: 12px;
  }
  .field-monthly-investment { margin-top: 13px; }
  .field-label { font-size: 11px; font-weight: 700; margin: 17px 0 0 1px; }
  .range { position: relative; height: 24px; margin-top: 7px; }
  .range .track { position: absolute; left: 2px; right: 0; top: 11px; height: 2px; background: var(--teal-dark); }
  .range .fill { position: absolute; left: 2px; width: 61px; top: 11px; height: 2px; background: var(--white); }
  .range .thumb { position: absolute; left: 54px; top: 3px; width: 18px; height: 18px; border-radius: 50%; background: #e8f7f8; }
  .field-one-time { margin-top: 16px; }
  .or { font-size: 11px; margin: 6px 0 0 2px; line-height: 18px; }
  .field-monthly-payment { margin-top: 6px; }
  .btn-invest {
    position: absolute; left: 259px; top: 272px; width: 187px; height: 41px; line-height: 41px;
    text-align: center; background: var(--accent); color: var(--white); font-size: 15px; font-weight: 500;
    letter-spacing: 0.4px; text-decoration: none; box-shadow: 6px 6px 0 var(--accent-shadow);
  }

  .footer-nav { position: absolute; top: 553px; left: 178px; display: flex; gap: 23px; }
  .footer-nav a { color: var(--ink); font-size: 14px; font-weight: 500; text-decoration: none; }

  .copyright {
    position: absolute; left: 0; top: 598px; width: 699px; height: 37px; background: var(--footer-bar);
    color: var(--white); font-size: 9px; text-align: center; line-height: 22px; padding-top: 0;
  }

  .benefit { position: absolute; top: 516px; width: 130px; text-align: center; }
  .benefit .badge {
    width: 78px; height: 78px; margin: 0 auto; border: 2.5px solid var(--teal); border-radius: 50%;
    display: flex; align-items: center; justify-content: center;
  }
  .benefit .badge .mark { width: 26px; height: 26px; border-radius: 50%; background: var(--teal); }
  .benefit p { margin-top: 15px; color: var(--accent); font-size: 11px; font-weight: 700; }
  .benefit-education { left: 727px; }
  .benefit-income { left: 869px; }
  .benefit-retirement { left: 1021px; }
</style>
</head>
<body>
  <header class="hero">
    <div class="brand">perovalstrinka</div>
    <nav class="account-nav">
      <a class="btn-small" href="#">SIGN IN</a>
      <a class="btn-small" href="#">SIGN UP</a>
    </nav>

    <section class="video-monitor">
      <div class="monitor-visual">
        <div class="screen" role="img" aria-label="Explainer video still: two colleagues reviewing investment charts on a laptop">
          <svg class="play-icon" width="76" height="76" viewBox="0 0 76 76" aria-hidden="true">
            <circle cx="38" cy="38" r="35" fill="none" stroke="#ffffff" stroke-width="4"/>
            <path d="M30 22 L56 38 L30 54 Z" fill="#ffffff"/>
          </svg>
        </div>
      </div>
      <div class="monitor-stand" role="img" aria-label="Monitor stand"></div>
    </section>

    <form class="calculator">
      <h1>OUR ONLINE CALCULATOR</h1>
      <span class="field field-monthly-investment">Regular monthly investment:</span>
      <div class="field-label">Length of investment</div>
      <div class="range"><span class="track"></span><span class="fill"></span><span class="thumb"></span></div>
      <span class="field field-one-time">One timepayment:</span>
      <div class="or">OR</div>
      <span class="field field-monthly-payment">Monthly payment:</span>
      <a class="btn-invest" href="#">I WANT TO INVEST</a>
    </form>
  </header>

  <nav class="footer-nav">
    <a href="#">About us</a>
    <a href="#">FAQ</a>
    <a href="#">Privacy Policy</a>
    <a href="#">Contact</a>
  </nav>
  <footer class="copyright">© 2017 perovalstrinka. All rights reserved.</footer>

  <div class="benefit benefit-education">
    <div class="badge"><span class="mark" role="img" aria-label="Apple on a book icon"></span></div>
    <p>Education for kids</p>
  </div>
  <div class="benefit benefit-income">
    <div class="badge">
      <svg width="36" height="32" viewBox="0 0 36 32" aria-hidden="true">
        <rect x="2" y="20" width="6" height="11" fill="#42b1bf"/>
        <rect x="11" y="15" width="6" height="16" fill="#42b1bf"/>
        <rect x="20" y="18" width="6" height="13" fill="#42b1bf"/>
        <rect x="29" y="10" width="6" height="21" fill="#42b1bf"/>
        <path d="M3 14 L12 7 L21 11 L32 2" fill="none" stroke="#42b1bf" stroke-width="2.2"/>
        <path d="M27 1 L33 1 L33 7" fill="none" stroke="#42b1bf" stroke-width="2.2"/>
      </svg>
    </div>
    <p>Passive income</p>
  </div>
  <div class="benefit benefit-retirement">
    <div class="badge"><span class="mark" role="img" aria-label="Palm island with setting sun icon"></span></div>
    <p>Happy retirment</p>
  </div>
</body>
</html>
```